Larkmoor Apartments Downtown Northport

We are looking to redesign our entry way sign at Larkmoor Apartments, a low density residential apartment building, located in Downtown Northport, Alabama, U.S. Downtown Northport is a bustling boutique business district with a small town feel comprised of shops, restaurants, and a renowned arts community known for Velloway Arts Center and Festival which is one of the nation's top outdoor arts festivals. Larkmoor Apartments and its sign is the first thing you seen when you enter Downtown Northport. We are looking to redesign our sign, entry way and landscaping to compliment the building and character of the historic downtown.

Target Market(s)

Our apartment building is comprised of 20 apartments units with tenants who are primarily part of the local workforce, young professionals, or students at the Tressdale University or other nearby institutions.

Requirements
Must have
• The name of the apartment building - Larkmoor
Phone number on the sign 205-555-0148

```html
<!DOCTYPE html>
<html lang="en">
<head>
<meta charset="utf-8">
<title>Larkmoor Apartments – Entry Sign</title>
<link rel="stylesheet" href="https://fonts.googleapis.com/css2?family=Cinzel:wght@400;500&display=swap">
<style>
  :root {
    --page-bg: #bab9cc;
    --sign-white: #ffffff;
    --sign-brown: #612914;
    --accent-gold: #c6ad6c;
    --text-gold: #d9c58f;
    --phone-gold: #b49b5c;
    --icon-red: #6d1411;
  }
  * { margin: 0; padding: 0; box-sizing: border-box; }
  html, body {
    width: 1200px;
    height: 1200px;
    overflow: hidden;
    background: var(--page-bg);
  }
  .canvas {
    position: relative;
    width: 1200px;
    height: 1200px;
  }
  .entry-sign {
    position: absolute;
    left: 100px;
    top: 300px;
    width: 1000px;
    height: 600px;
    background: var(--sign-white);
    box-shadow: 0 6px 18px rgba(60, 55, 80, 0.28);
    overflow: hidden;
  }
  .sign-backdrop {
    position: absolute;
    inset: 0;
    width: 100%;
    height: 100%;
  }
  .property-name {
    position: absolute;
    left: 0;
    right: 0;
    top: 73px;
    text-align: center;
    font-family: "Cinzel", "Trajan Pro", serif;
    font-weight: 400;
    font-size: 126px;
    letter-spacing: 6px;
    line-height: 1;
    white-space: nowrap;
    color: var(--text-gold);
  }
  .property-name .initial { font-size: 158px; }
  .phone-badge {
    position: absolute;
    left: 69px;
    top: 454px;
    width: 120px;
    height: 120px;
  }
  .phone-number {
    position: absolute;
    left: 245px;
    top: 475px;
    font-family: "Cinzel", "Trajan Pro", serif;
    font-weight: 400;
    font-size: 100px;
    letter-spacing: 3px;
    line-height: 1;
    white-space: nowrap;
    color: var(--phone-gold);
  }
</style>
</head>
<body>
  <main class="canvas">
    <section class="entry-sign" aria-label="Larkmoor Apartments entry sign">
      <svg class="sign-backdrop" viewBox="0 0 1000 600" preserveAspectRatio="none" aria-hidden="true">
        <defs>
          <linearGradient id="swoosh-gold" x1="0" y1="0" x2="1" y2="0">
            <stop offset="0" stop-color="#d8c893"/>
            <stop offset="0.6" stop-color="#c6ad6c"/>
            <stop offset="1" stop-color="#a98f4c"/>
          </linearGradient>
        </defs>
        <path class="brown-field" fill="#612914"
              d="M0 0 H1000 V275 C850 360 650 398 450 394 C280 390 120 340 0 270 Z"/>
        <path class="gold-swoosh" fill="url(#swoosh-gold)"
              d="M155 362 C400 432 750 422 1000 334 V284 C800 390 480 418 155 362 Z"/>
      </svg>

      <h1 class="property-name"><span class="initial">L</span>ARKMOOR</h1>

      <svg class="phone-badge" viewBox="0 0 124 124" aria-hidden="true">
        <circle cx="62" cy="62" r="59" fill="none" stroke="#c6ad6c" stroke-width="5"/>
        <circle cx="62" cy="62" r="45" fill="#6d1411"/>
        <path fill="#ffffff"
              d="M48 44 c3-3 6-2 7 1 l3 7 c1 2 0 4-2 5 l-3 2 c2 5 6 9 11 11 l2-3 c1-2 3-3 5-2 l7 3 c3 1 4 4 1 7 l-3 3 c-4 4-13 2-23-8 c-10-10-12-19-8-23 Z"/>
        <path fill="none" stroke="#ffffff" stroke-width="3" stroke-linecap="round"
              d="M66 46 a12 12 0 0 1 12 12 M66 38 a20 20 0 0 1 20 20"/>
      </svg>
      <p class="phone-number">205-555-0148</p>
    </section>
  </main>
</body>
</html>
```